Super elegant, crisp & clean Business card design required

We recently upgraded our branding - which is on our website - tavorelstudio.com

I would like a simple, yet elegant, clean business card design please.

The font of my logo is Cinzel - and because of the natural colour - it's best to have this on a black background.

I would like to have the back of the business card - with simply my logo.

PLEASE DO NOT SUBMIT A COMPLICATED / UNCLEAN DESIGN

Industry/Entity Type

Business

Contact Information for Business Card

Dalvik Ostrander Photography

Font styles to use
Other font styles liked:
• Cinzel

Requirements
Must have
• A backpage with nothing but my logo
• Simple design - stands out
Should not have
• Colour that dont align with my logo
• Over complicated '/ non symmetrical design

```html
<!DOCTYPE html>
<html lang="en">
<head>
<meta charset="utf-8">
<title>Dalvik Ostrander Photography – Business Card</title>
<link href="https://fonts.googleapis.com/css2?family=Cinzel:wght@400&family=Open+Sans:wght@400&display=swap" rel="stylesheet">
<style>
  :root {
    --backdrop: #5a3433;
    --card: #000000;
    --gold: #8c7b62;
    --gold-soft: #7d6e58;
    --shadow: rgba(0, 0, 0, 0.45);
  }
  * { margin: 0; padding: 0; box-sizing: border-box; }
  html, body {
    width: 1200px; height: 1200px; overflow: hidden;
    background: var(--backdrop);
  }
  .canvas { position: relative; width: 1200px; height: 1200px; }
  .card {
    position: absolute; left: 306px; width: 588px; height: 333px;
    background: var(--card); border-radius: 16px;
    box-shadow: 0 4px 8px var(--shadow);
  }
  .card--front { top: 222px; }
  .card--back { top: 646px; }

  .brand-mark {
    position: absolute; border: 1.5px solid var(--gold); border-radius: 50%;
  }
  .card--front .brand-mark { left: 236px; top: 74px; width: 116px; height: 116px; }
  .card--back .brand-mark { left: 456px; top: 48px; width: 80px; height: 80px; }

  .wordmark {
    position: absolute; left: 0; right: 0; top: 216px; text-align: center;
    color: var(--gold); font-family: "Cinzel", serif;
  }
  .wordmark__name { font-size: 27px; line-height: 32px; letter-spacing: 0.5px; }
  .wordmark__tag {
    font-size: 11px; letter-spacing: 9.5px; margin-top: 2px; padding-left: 9px;
  }

  .mark-name {
    position: absolute; left: 416px; width: 160px; top: 136px; text-align: center;
    font-family: "Cinzel", serif; color: var(--gold); font-size: 12px; letter-spacing: 1px;
  }

  .accent-bar {
    position: absolute; left: 0; top: 202px; width: 12px; height: 26px;
    background: var(--gold-soft);
  }
  .person {
    position: absolute; left: 30px; top: 196px;
    font-family: "Cinzel", serif; color: var(--gold); font-size: 26px; line-height: 36px;
  }
  .contact {
    position: absolute; left: 30px; top: 244px; list-style: none;
    font-family: "Open Sans", sans-serif; color: var(--gold); font-size: 15.5px;
  }
  .contact__item { display: flex; align-items: center; height: 22.5px; }
  .contact__icon { width: 14px; height: 14px; margin-right: 8px; fill: var(--gold); }
</style>
</head>
<body>
<main class="canvas">
  <section class="card card--front" aria-label="Card front">
    <div class="brand-mark"></div>
    <div class="wordmark">
      <div class="wordmark__name">Dalvik Ostrander</div>
      <div class="wordmark__tag">PHOTOGRAPHY</div>
    </div>
  </section>

  <section class="card card--back" aria-label="Card back">
    <div class="brand-mark"></div>
    <div class="mark-name">Dalvik Ostrander</div>
    <div class="accent-bar"></div>
    <div class="person">Dalvik Ostrander</div>
    <ul class="contact">
      <li class="contact__item">
        <svg class="contact__icon" viewBox="0 0 16 16"><path d="M1 5c0-2 3-3 7-3s7 1 7 3v1h-3V5c0-.8-2-1.2-4-1.2S4 4.2 4 5v1H1z"/><path d="M3 7h10l1 7H2z"/><circle cx="8" cy="10.5" r="1.8" fill="#000"/></svg>
        000.0000
      </li>
      <li class="contact__item">
        <svg class="contact__icon" viewBox="0 0 16 16"><path d="M1 3h14v10H1z"/><path d="M1.5 3.5 8 9l6.5-5.5" stroke="#000" stroke-width="1.3" fill="none"/></svg>
        contact@tavorelstudio.com
      </li>
      <li class="contact__item">
        <svg class="contact__icon" viewBox="0 0 16 16"><circle cx="8" cy="8" r="6.5" fill="none" stroke="var(--gold)" stroke-width="1.2"/><ellipse cx="8" cy="8" rx="2.8" ry="6.5" fill="none" stroke="var(--gold)" stroke-width="1.1"/><path d="M1.5 8h13M2.5 5h11M2.5 11h11" stroke="var(--gold)" stroke-width="1"/></svg>
        www.tavorelstudio.com
      </li>
    </ul>
  </section>
</main>
</body>
</html>
```